Healthcare patient advocacy company needs banner for conference booth

We need a banner to hang behind us in our booth at conferences. I would like something that prominently features our company name - brovint LLC. And also includes the following language: No employee should face medical debt alone. No Plan should be unrepresented. Expert advocacy and legal support from first bill to final resolution. The colors we use for our other materials are HEX 002C45, FECC73, 00C6CF, E0D5B9, 004C66. And the font is Epilogue. I would welcome some graphics, but no scales of justice or dollar bills or anything like that. I'm attaching some materials so you can see one of our brochures.

Target Market(s)

B2B - health insurers, third-party health care administrators, cost-containment companies

Industry/Entity Type

Healthcare Advocacy

Requirements
Must have
• Name prominently displayed and taglines in project description.
Nice to have
• I would like something easy to read and eye-catching that is not overly complicated or cutsey.
Should not have
• Scales of justice or dollar signs.

```html
<!DOCTYPE html>
<html lang="en">
<head>
<meta charset="utf-8">
<title>brovint — Booth Banner</title>
<link href="https://fonts.googleapis.com/css2?family=Barlow+Condensed:wght@600&family=Epilogue:wght@300;400;700&display=swap" rel="stylesheet">
<style>
  :root {
    --navy: #002C45;
    --navy-deep: #001A2E;
    --navy-mid: #0A3A66;
    --gold: #FECC73;
    --gold-deep: #E2A94E;
    --teal: #00C6CF;
    --sand: #E0D5B9;
    --petrol: #004C66;
    --cream: #FFF8EC;
    --ink-light: #DCE6F0;
  }
  * { box-sizing: border-box; margin: 0; padding: 0; }
  html, body {
    width: 1200px;
    height: 1049px;
    overflow: hidden;
    background: var(--navy-deep);
  }
  .banner {
    position: relative;
    width: 1200px;
    height: 1049px;
    overflow: hidden;
    font-family: "Epilogue", sans-serif;
    color: var(--ink-light);
  }
  .banner__backdrop {
    position: absolute;
    inset: 0;
    background:
      radial-gradient(ellipse 70% 60% at 55% 40%, rgba(20, 70, 130, 0.55), transparent 70%),
      linear-gradient(90deg, #000A14 0%, var(--navy-mid) 22%, #0B3D70 55%, var(--navy) 85%, #000A14 100%);
  }
  .banner__backdrop::after {
    content: "";
    position: absolute;
    inset: 0;
    background: linear-gradient(180deg, rgba(0,0,0,0) 55%, rgba(0,10,25,0.55) 100%);
  }
  .brand-name {
    position: absolute;
    top: 28px;
    left: 0;
    width: 100%;
    text-align: center;
    font-weight: 700;
    font-size: 84px;
    letter-spacing: -2px;
    color: var(--cream);
  }
  .headline {
    position: absolute;
    top: 150px;
    left: 0;
    width: 100%;
    text-align: center;
    font-family: "Barlow Condensed", sans-serif;
    font-weight: 600;
    font-size: 100px;
    line-height: 0.95;
    text-transform: uppercase;
    letter-spacing: 0.5px;
    color: var(--gold);
    background: linear-gradient(90deg, var(--gold-deep) 0%, var(--gold) 50%, var(--gold-deep) 100%);
    -webkit-background-clip: text;
    background-clip: text;
    -webkit-text-fill-color: transparent;
  }
  .subline {
    position: absolute;
    top: 380px;
    left: 0;
    width: 100%;
    text-align: center;
    font-weight: 300;
    font-size: 30px;
    line-height: 1.38;
    color: var(--ink-light);
  }
  .web-address {
    position: absolute;
    top: 672px;
    left: 0;
    width: 100%;
    padding-left: 20px;
    text-align: center;
    font-weight: 400;
    font-size: 36px;
    color: var(--gold);
  }
  .accent-area {
    position: absolute;
    left: 882px;
    top: 548px;
    width: 318px;
    height: 501px;
    background:
      linear-gradient(160deg,
        rgba(0, 198, 207, 0.55) 0%,
        rgba(224, 213, 185, 0.45) 35%,
        rgba(254, 204, 115, 0.45) 65%,
        rgba(0, 76, 102, 0.55) 100%);
    border-top-left-radius: 160px;
  }
</style>
</head>
<body>
  <main class="banner">
    <div class="banner__backdrop" role="img" aria-label="Dim blue-toned photograph of a surgical team at work, overlaid with soft translucent circles"></div>

    <div class="brand-name">brovint</div>

    <h1 class="headline">No employee should<br>face medical debt alone.</h1>

    <p class="subline">No Plan should be unrepresented. Expert advocacy and legal<br>support from first bill to final resolution.</p>

    <p class="web-address">brovinthealth.com</p>

    <div class="accent-area" role="img" aria-label="Decorative cluster of geometric shapes in teal, sand, gold and petrol"></div>
  </main>
</body>
</html>
```